Business card design needed for rebranded top-end landscaping business

We need a new business card design, incorporating our logo (colours Green #8dc63f and Grey #8a8c8e) and also some options that include the colour dark navy (eg #000040) as our uniforms are navy with white and grey trim.

We are an innovative landscaping company that maintains high-end gardens for meticulous clients. We pride ourselves on our customer service, our professionalism, and our workmanship.

Our business name needs to be easily read and our branding needs to be bold and memorable, without screaming "tradesman"! We prefer clean lines over lots of fine detail.

The design MUST include:
- Business name ("Brambleton Gardenworks")
- Logo (file uploaded)
- Employee name
- Phone number
- Email address
- www.brambletongardenworks.com.au
- Pagebook & Snapgrid logos
- The Turfcraft Guild logo (file uploaded) along with the word "Member"
- Licence "Lic. 618392K"

OPTIONAL inclusions:
- "Creating outdoor spaces for our community to be inspired, refreshed and re-energised"
- "Landscape Maintenance - Irrigation - Arboriculture" (dashes can be replaced with dots or other)
- "Fully qualified, licensed & insured"
- "Residential - Strata - Commercial - Real Estate" (dashes can be replaced with dots or other)

High-end professionals and retirees, real estate agents

Landscaping

See Project description

Sans Serif

Designer to choose colors to be used in the design.

• Must incorporate our logo, and colours Green #8dc63f and Grey #8a8c8e) from the logo, and the colour DARK NAVY (eg #000040).
• The design MUST include:
• - Business name ("Brambleton Gardenworks")
• - Logo (file uploaded)
• - Employee name
• - Phone number
• - Email address
• - www.brambletongardenworks.com.au
• - Pagebook & Snapgrid logos
• - The Turfcraft Guild logo (file uploaded) along with the word "Member"
• - Licence "Lic. 618392K"
• OPTIONAL inclusions:
• - "Creating outdoor spaces for our community to be inspired, refreshed and re-energised"
• - "Landscape Maintenance - Irrigation - Arboriculture" (dashes can be replaced with dots or other)
• - "Fully qualified, licensed & insured"
• - "Residential - Strata - Commercial - Real Estate" (dashes can be replaced with dots or other)

```html
<!DOCTYPE html>
<html lang="en">
<head>
<meta charset="utf-8">
<title>Brambleton Gardenworks – Business Card</title>
<link href="https://fonts.googleapis.com/css2?family=Roboto:wght@400;500&display=swap" rel="stylesheet">
<style>
  :root {
    --backdrop: #d9dadc;
    --paper: #ffffff;
    --navy: #0e0e3e;
    --green: #8dc63f;
    --grey: #8a8c8e;
    --label: #555555;
  }
  * { margin: 0; padding: 0; box-sizing: border-box; }
  html, body { width: 1200px; height: 750px; overflow: hidden; }
  body {
    background: var(--backdrop);
    font-family: "Roboto", Arial, sans-serif;
    position: relative;
  }
  .card {
    position: absolute;
    top: 225px;
    width: 525px;
    height: 300px;
  }
  .card--front { left: 53px; background: var(--paper); }
  .card--back { left: 622px; background: var(--navy); }

  .employee-name {
    position: absolute; left: 41px; top: 38px;
    font-size: 28px; font-weight: 400; color: var(--navy);
    letter-spacing: -0.3px;
  }
  .employee-name span { color: var(--green); }

  .contact { position: absolute; left: 41px; top: 74px; list-style: none; }
  .contact li {
    display: flex; align-items: center; gap: 6px;
    font-size: 14.5px; color: var(--grey); height: 19px;
  }
  .contact svg { flex: none; }

  .brand {
    position: absolute; display: flex; flex-direction: column; align-items: center;
  }
  .brand__mark { width: 48px; height: 48px; border-radius: 50%; background: var(--grey); margin-bottom: 6px; }
  .brand__name {
    font-size: 19px; font-weight: 500; color: var(--green);
    line-height: 1.1; text-align: center;
  }
  .card--front .brand { left: 340px; top: 33px; width: 150px; }
  .card--back .brand { left: 187px; top: 87px; width: 150px; }

  .membership {
    position: absolute; left: 41px; top: 182px; width: 120px;
    display: flex; flex-direction: column; align-items: center;
  }
  .membership__label { font-size: 14px; color: var(--label); }
  .membership__badge { width: 26px; height: 26px; background: var(--green); margin: 8px 0 30px; }
  .membership__licence { font-size: 14px; color: var(--navy); }

  .social { position: absolute; right: 43px; top: 246px; display: flex; gap: 8px; }
  .social span {
    display: flex; align-items: center; gap: 3px;
    font-size: 10px; color: var(--grey);
  }
  .social i { width: 10px; height: 10px; background: var(--grey); display: inline-block; }

  .website {
    position: absolute; right: 41px; top: 265px;
    font-size: 14px; color: var(--grey);
  }

  .tagline {
    position: absolute; left: 0; right: 0; top: 201px;
    text-align: center; font-size: 14px; letter-spacing: 4.2px;
    color: var(--grey);
  }
</style>
</head>
<body>
  <section class="card card--front">
    <h1 class="employee-name">Employee <span>Name</span></h1>
    <ul class="contact">
      <li>
        <svg width="11" height="16" viewBox="0 0 11 16" fill="none" stroke="#8dc63f" stroke-width="1"><rect x="1" y="0.5" width="9" height="15" rx="1.5"/><line x1="1" y1="12" x2="10" y2="12"/><line x1="1" y1="2.5" x2="10" y2="2.5"/></svg>
        0962 418573
      </li>
      <li>
        <svg width="13" height="10" viewBox="0 0 13 10" fill="none" stroke="#8dc63f" stroke-width="1"><rect x="0.5" y="0.5" width="12" height="9"/><polyline points="0.5,0.5 6.5,5.5 12.5,0.5"/></svg>
        email@brambletongardenworks.com.au
      </li>
    </ul>

    <div class="brand">
      <div class="brand__mark"></div>
      <div class="brand__name">Brambleton<br>Gardenworks</div>
    </div>

    <div class="membership">
      <p class="membership__label">Member</p>
      <div class="membership__badge" role="img" aria-label="The Turfcraft Guild badge"></div>
      <p class="membership__licence">Lic. 618392K</p>
    </div>

    <div class="social">
      <span><i></i>Pagebook</span>
      <span><i></i>Snapgrid</span>
    </div>
    <p class="website">www.brambletongardenworks.com.au</p>
  </section>

  <section class="card card--back">
    <div class="brand">
      <div class="brand__mark"></div>
      <div class="brand__name">Brambleton<br>Gardenworks</div>
    </div>
    <p class="tagline">FULLY QUALIFIED, LICENSED &amp; INSURED</p>
  </section>
</body>
</html>
```